e-commerce store for sport clothing online store "baseball merchandise "web application...

I want to design a UX/UI for my web application website for the online store I will provide you with the following:
1. screen shots of the initial design for the pages>
2. the logo files.
3. The brand guideline file.

the provided files (screen shots) is guideline I want to see CREATIVITY with the UX/UI DESIGN.
PS. PLEASE FOLLOW THE BRANDGUIDE LINE CAREFULLY SPECIALLY THE TYPOGRAPHY & THE COLOR CODES.

PLEASE VISIT THIS WEBSITE morningpath.velrin-qz.com to see more for the screens.

```html
<!DOCTYPE html>
<html lang="en">
<head>
<meta charset="UTF-8">
<title>Checkout – Payment Details</title>
<link rel="stylesheet" href="https://fonts.googleapis.com/css2?family=Exo+2:wght@600;700&family=Lato:wght@400;700&display=swap">
<style>
  :root {
    --navy: #0f2447;
    --page-bg: #e9ecf1;
    --screen-bg: #ffffff;
    --card-bg: #d9d9d9;
    --text: #111111;
    --button: #000000;
    --white: #ffffff;
  }
  * { box-sizing: border-box; margin: 0; padding: 0; }
  html, body {
    width: 859px; height: 1200px; overflow: hidden;
    background: var(--page-bg);
    font-family: "Lato", Arial, sans-serif;
    color: var(--text);
  }
  .screen {
    position: absolute; left: 159px; top: 0;
    width: 540px; height: 1200px;
    background: var(--screen-bg);
    overflow: hidden;
  }
  .app-bar {
    height: 121px; background: var(--navy);
    display: flex; align-items: center; justify-content: center;
    position: relative;
  }
  .app-bar__back { position: absolute; left: 36px; top: 47px; width: 28px; height: 28px; }
  .app-bar__title {
    font-family: "Exo 2", Arial, sans-serif; font-weight: 700;
    font-size: 25px; color: var(--white); margin-top: -2px;
  }
  .stepper { position: relative; height: 220px; }
  .stepper__line {
    position: absolute; top: 203px; height: 2px; background: var(--navy);
  }
  .step { position: absolute; top: 175px; width: 150px; margin-left: -75px; text-align: center; }
  .step__dot {
    width: 57px; height: 57px; border-radius: 50%; margin: 0 auto;
    display: flex; align-items: center; justify-content: center;
    font-family: "Exo 2", Arial, sans-serif; font-weight: 700; font-size: 28px;
    background: var(--navy); color: var(--white); border: 2px solid var(--navy);
  }
  .step--todo .step__dot { background: var(--white); color: var(--navy); }
  .step__label { margin-top: 8px; font-size: 18px; line-height: 23px; color: var(--navy); }
  .section-title {
    position: absolute; left: 21px; top: 329px;
    font-weight: 700; font-size: 23px;
  }
  .pay-option {
    position: absolute; left: 21px; width: 498px; height: 88px;
    background: var(--card-bg); border-radius: 8px;
    display: flex; align-items: center; padding: 0 18px 0 29px;
  }
  .pay-option--first { top: 380px; }
  .pay-option--second { top: 492px; }
  .pay-option__radio { width: 28px; height: 28px; flex: none; }
  .pay-option__name { margin-left: 24px; font-size: 22px; flex: 1; }
  .pay-option__mark {
    display: flex; align-items: center; gap: 6px;
    font-size: 14px; font-weight: 700; color: var(--navy);
  }
  .pay-option__mark i { width: 12px; height: 12px; background: var(--navy); display: block; }
  .action-bar {
    position: absolute; left: 0; right: 0; top: 1108px; bottom: 0;
    background: var(--white); border-radius: 14px 14px 0 0;
    box-shadow: 0 -6px 14px rgba(0,0,0,0.12);
  }
  .action-bar__button {
    position: absolute; left: 18px; right: 16px; top: 12px; height: 66px;
    background: var(--button); color: var(--white); border: 0; border-radius: 6px;
    font-family: "Lato", Arial, sans-serif; font-weight: 700; font-size: 20px;
  }
</style>
</head>
<body>
  <main class="screen">
    <header class="app-bar">
      <svg class="app-bar__back" viewBox="0 0 24 24" fill="none" stroke="#fff" stroke-width="2.4" stroke-linecap="round" stroke-linejoin="round">
        <path d="M21 12H4M11 4l-8 8 8 8"/>
      </svg>
      <h1 class="app-bar__title">Checkout</h1>
    </header>

    <section class="stepper" style="position:absolute;left:0;top:0;width:540px;">
      <div class="stepper__line" style="left:118px;width:152px;"></div>
      <div class="stepper__line" style="left:270px;width:153px;"></div>
      <div class="step" style="left:118px;">
        <div class="step__dot">1</div>
        <p class="step__label">Shipping<br>Details</p>
      </div>
      <div class="step" style="left:270px;">
        <div class="step__dot">2</div>
        <p class="step__label">Payment<br>Details</p>
      </div>
      <div class="step step--todo" style="left:423px;">
        <div class="step__dot">3</div>
        <p class="step__label">Confirmation</p>
      </div>
    </section>

    <h2 class="section-title">Payment Method</h2>

    <div class="pay-option pay-option--first">
      <svg class="pay-option__radio" viewBox="0 0 28 28">
        <circle cx="14" cy="14" r="14" fill="var(--navy)"/>
        <path d="M8 14.5l4 4 8-9" fill="none" stroke="#fff" stroke-width="2.6" stroke-linecap="round" stroke-linejoin="round"/>
      </svg>
      <span class="pay-option__name">Netlink</span>
      <span class="pay-option__mark"><i></i>Netlink</span>
    </div>

    <div class="pay-option pay-option--second">
      <svg class="pay-option__radio" viewBox="0 0 28 28">
        <circle cx="14" cy="14" r="12.8" fill="none" stroke="var(--navy)" stroke-width="2.2"/>
      </svg>
      <span class="pay-option__name">Cardline/Paycirc</span>
      <span class="pay-option__mark">Paycirc&nbsp; Cardline</span>
    </div>

    <footer class="action-bar">
      <button class="action-bar__button">Proceed</button>
    </footer>
  </main>
</body>
</html>
```